BrivoPeak Business Card Design Project

We are looking for a modern, clean business card design for our new company. We are a consulting firm focused on the financial services market providing management and IT consulting to banks, insurance companies, etc. Please include our company logo and company contact information from the attached file in the design. Two versions of the logo are attached, either version is acceptable. Logos are available in other file formats if needed. We would like to include the contact information for both our UK and US offices as well as the following information for each individual card holder: Name, position/title, address, phone number and e-mail address.
Updates
Project Deadline Extended
Reason: A last minute trip over seas has prevented us from finalizing the decision. A decision will be made this week. We apologize for the inconvenience.
Industry/Entity Type
Business
Contact Information for Business Card
Company logo.
Company locations and phone numbers for both the US and UK offices.
Company URL.
Cardholder Name
Cardholder Position/title
Cardholder Address
Cardholder Phone Number
Cardholder e-mail Address
Look and feel
Each slider illustrates characteristics of the customer's brand and the style your logo design should communicate.

```html
<!DOCTYPE html>
<html lang="en">
<head>
<meta charset="utf-8">
<title>BrivoPeak Partners – Business Cards</title>
<link href="https://fonts.googleapis.com/css2?family=Open+Sans:wght@400;600;700&display=swap" rel="stylesheet">
<style>
  :root {
    --page-bg: #d9d9d9;
    --card-white: #ffffff;
    --card-grey: #676767;
    --brand-navy: #1d355e;
    --ink-light: #f2f2f2;
    --seam: #e6e6e6;
  }
  * { box-sizing: border-box; margin: 0; padding: 0; }
  html, body {
    width: 1200px; height: 900px; overflow: hidden;
    background: var(--page-bg);
    font-family: "Open Sans", Arial, sans-serif;
  }
  .sheet { position: relative; width: 1200px; height: 900px; }
  .card {
    position: absolute; left: 250px; width: 700px; height: 400px;
    background: var(--card-white);
    box-shadow: 0 6px 18px rgba(0,0,0,.18);
    overflow: hidden;
  }
  .card--back { top: 35px; }
  .card--front { top: 465px; }

  .brand-name {
    color: var(--brand-navy);
    font-weight: 700;
    font-size: 50px;
    letter-spacing: -0.5px;
    display: flex; align-items: center; gap: 14px;
    white-space: nowrap;
  }
  .brand-mark {
    width: 22px; height: 22px; background: var(--brand-navy); flex: none;
  }

  /* Back card */
  .back-head {
    position: absolute; left: 0; top: 0; width: 100%; height: 172px;
    background: var(--card-white);
  }
  .back-head .brand-name { position: absolute; left: 120px; top: 52px; }
  .back-head .site {
    position: absolute; left: 290px; top: 138px;
    font-size: 15px; color: var(--brand-navy); font-weight: 600;
    letter-spacing: .3px;
  }
  .back-seam {
    position: absolute; left: 0; top: 172px; width: 100%; height: 18px;
    background: linear-gradient(#ffffff, var(--seam));
    box-shadow: 0 3px 5px rgba(0,0,0,.18);
    z-index: 1;
  }
  .back-body {
    position: absolute; left: 0; top: 190px; width: 100%; height: 210px;
    background: var(--card-grey); color: var(--ink-light);
    font-size: 15px; line-height: 1.25;
  }
  .office { position: absolute; font-style: normal; }
  .office--uk { right: 34px; top: 14px; text-align: right; }
  .office--us { left: 34px; bottom: 40px; }

  /* Front card */
  .front-logo-panel {
    position: absolute; left: 0; top: 0; width: 300px; height: 100%;
    background: var(--card-white);
    box-shadow: 4px 0 8px rgba(0,0,0,.2);
    z-index: 1;
    display: flex; align-items: center; justify-content: center;
    padding: 0 24px;
  }
  .front-logo-panel .brand-name { font-size: 36px; gap: 12px; line-height: 1.1; }
  .front-logo-panel .brand-mark { width: 16px; height: 16px; }
  .brand-lines { display: flex; flex-direction: column; }
  .front-info {
    position: absolute; left: 300px; top: 0; right: 0; height: 100%;
    background: var(--card-grey); color: var(--ink-light);
    text-align: right; padding: 54px 30px 0 0;
  }
  .holder-name {
    font-size: 25px; font-weight: 700; color: #fff; letter-spacing: .5px;
    line-height: 1.1;
  }
  .holder-title { font-size: 13px; letter-spacing: .8px; margin-bottom: 12px; }
  .contact-list { list-style: none; font-size: 15px; line-height: 1.3; }
  .contact-list li { display: flex; justify-content: flex-end; align-items: center; gap: 8px; }
  .contact-list .icon { width: 13px; height: 13px; flex: none; }
  .contact-list .spacer { width: 13px; flex: none; }
</style>
</head>
<body>
<main class="sheet">

  <section class="card card--back" aria-label="Card back">
    <div class="back-head">
      <div class="brand-name"><span class="brand-mark"></span>BrivoPeak Partners</div>
      <div class="site">www.brivopeakpartners.com</div>
    </div>
    <div class="back-seam"></div>
    <div class="back-body">
      <address class="office office--uk">
        14-16 Marlow Street<br>
        London E2 4QT Great Britain<br>
        UK +44 7700 900412
      </address>
      <address class="office office--us">
        418 N Larkspur Way, Suite 204-209<br>
        Fairview UT 84629 United States<br>
        US (801) 555-0143
      </address>
    </div>
  </section>

  <section class="card card--front" aria-label="Card front">
    <div class="front-logo-panel">
      <div class="brand-name"><span class="brand-mark"></span><span class="brand-lines"><span>BrivoPeak</span><span>Partners</span></span></div>
    </div>
    <div class="front-info">
      <h1 class="holder-name">ELIN MARSH</h1>
      <p class="holder-title">DIRECTOR</p>
      <ul class="contact-list">
        <li>2207-18 Bayview<span class="spacer"></span></li>
        <li>Hamilton, Ontario UK<span class="spacer"></span></li>
        <li>(801) 555-0143
          <svg class="icon" viewBox="0 0 16 16" aria-hidden="true"><path fill="#fff" d="M3.5 1.5l2.5 2.6-1.4 2a8 8 0 0 0 5.3 5.3l2-1.4 2.6 2.5-1.5 2C7 14.3 1.7 9 1.5 3z"/></svg></li>
        <li>+44 7700 900412
          <svg class="icon" viewBox="0 0 16 16" aria-hidden="true"><rect x="4" y="1" width="8" height="14" rx="1.5" fill="none" stroke="#fff" stroke-width="1.6"/><circle cx="8" cy="12.3" r="1" fill="#fff"/></svg></li>
        <li>elin@norvelcapital.com
          <svg class="icon" viewBox="0 0 16 16" aria-hidden="true"><rect x="1.5" y="3.5" width="13" height="9" fill="none" stroke="#fff" stroke-width="1.5"/><path d="M1.5 3.5L8 9l6.5-5.5" fill="none" stroke="#fff" stroke-width="1.5"/></svg></li>
        <li>www.brivopeakpartners.com
          <svg class="icon" viewBox="0 0 16 16" aria-hidden="true"><g fill="none" stroke="#fff" stroke-width="1.3"><circle cx="8" cy="8" r="6.3"/><ellipse cx="8" cy="8" rx="2.8" ry="6.3"/><path d="M1.7 8h12.6"/></g></svg></li>
      </ul>
    </div>
  </section>

</main>
</body>
</html>
```